Looking for copywriting of the entire website + new selection of pictures

Hello,
My website's copy write is on the weaker side, so I'm looking for an entire re-do of my website's copy write. If you think a line is weak, re-write, otherwise you can leave it as is. We want our site to clearly explain what our events are, how they work, and why someone should sign up for them, while appealing to the hopeful, romantic, and nostalgic feelings of the visitors. Our speed dating events can be imagined as a modern day approach to the old-fashioned way of dating, where people got to know each other in person, away from the dating apps!! Additionally, I feel nearly all the existing pictures are rather weak, so please select entirely new pictures which give the website a less amateur feel, while retaining the playful nature of the brand. If there are areas where you think that section would benefit from no pictures at all, please communicate that.
Let me know if there are any further questions and thank you!
You can find the site at:
https://www.larkspindate.com
Industry/Entity Type
Speed Dating/Romance
Number of Pages Required
1 page
Look and feel
Each slider illustrates characteristics of the customer's brand and the style your logo design should communicate.

```html
<!DOCTYPE html>
<html lang="en">
<head>
<meta charset="utf-8">
<title>Larkspin Date – Home page concepts</title>
<link rel="stylesheet" href="https://fonts.googleapis.com/css2?family=Nunito:wght@500;600;700&family=Roboto:wght@400;500&display=swap">
<style>
:root{
  --board:#ababab;
  --white:#ffffff;
  --pink:#fbc9dd;
  --pink-soft:#fde3ee;
  --pink-label:#f5bcd3;
  --pink-line:#f29bbd;
  --ink:#1a1a1a;
  --muted:#555555;
  --grey:#f4f4f4;
  --night:#0e0e0e;
  --line-dark:#3a3a3a;
  --light:#dddddd;
}
*{box-sizing:border-box;margin:0;padding:0}
html,body{width:827px;height:1200px;overflow:hidden}
body{background:var(--board);position:relative;font-family:"Roboto",sans-serif;color:var(--ink)}
.page{position:absolute;top:61px;width:632px;height:2080px;transform:scale(0.5175);transform-origin:0 0;background:var(--white);overflow:hidden}
.page--a{left:61px}
.page--b{left:438px}
.abs{position:absolute}

/* header */
.topline{left:0;top:0;width:632px;height:3px;background:var(--pink)}
.brand{left:70px;top:14px;display:flex;align-items:center;gap:6px;font-family:"Nunito",sans-serif;font-weight:700;font-size:15px;color:var(--ink)}
.brand-dot{width:12px;height:12px;border-radius:50%;background:var(--pink-line)}
.contact-item{top:12px;display:flex;gap:8px;align-items:center}
.contact-item svg{width:20px;height:20px}
.contact-item small{display:block;font-size:6px;color:var(--muted)}
.contact-item b{display:block;font-size:8px;font-weight:500}
.socials{left:486px;top:14px;display:flex;gap:5px}
.socials span{width:19px;height:19px;border-radius:50%;background:var(--pink);display:flex;align-items:center;justify-content:center}
.socials span::after{content:"";width:6px;height:6px;border-radius:50%;background:var(--ink)}
.nav{left:168px;top:43px;width:464px;height:21px;background:var(--pink);clip-path:polygon(14px 0,100% 0,100% 100%,0 100%)}
.nav a{position:absolute;top:5px;font-size:7.5px;color:var(--ink);text-decoration:none}

/* hero */
.hero-photo{left:0;top:64px;width:632px;height:296px}
.page--a .hero-photo{background:linear-gradient(120deg,#b9b874 0%,#d8d3a2 40%,#c29a7c 62%,#6f8aa6 85%,#a8b9c4 100%)}
.page--b .hero-photo{background:linear-gradient(110deg,#e7e7e5 0%,#cfd1d2 40%,#c9423a 58%,#d6a35a 66%,#6c8fb5 82%,#8aa0b2 100%)}
.hero-title{left:76px;top:150px;font-family:"Nunito",sans-serif;font-weight:600;font-size:19px;letter-spacing:.2px}
.hero-sub{left:76px;top:188px;font-size:7.5px}
.btn{display:inline-flex;align-items:center;gap:4px;border-radius:12px;font-size:7.5px;font-weight:500;padding:6px 14px}
.btn svg{width:7px;height:7px}
.hero-btn{left:76px;top:220px;background:var(--pink);color:var(--ink)}

.card{top:330px;width:152px;height:90px;background:var(--white);box-shadow:0 1px 4px rgba(0,0,0,.12);text-align:center;font-family:"Nunito",sans-serif;font-weight:600;font-size:7.5px;padding-top:20px}
.card svg{display:block;margin:0 auto 8px;width:26px;height:26px}
.card--active{background:var(--pink)}
.intro{left:74px;top:444px;width:484px;text-align:center;font-size:6.5px;line-height:1.7;color:var(--muted)}

.section-title{width:632px;left:0;text-align:center;font-family:"Nunito",sans-serif;font-weight:600;font-size:18px}
.rule{height:2px;left:281px;width:70px;background:var(--pink-line)}
.code-icon{top:554px;height:52px}
.dash{top:580px;width:80px;border-top:1px dashed #777}
.step-num{top:616px;width:36px;height:36px;border-radius:50%;background:var(--pink);font-family:"Nunito",sans-serif;font-weight:600;font-size:16px;display:flex;align-items:center;justify-content:center}
.step-title{top:628px;font-size:8px;font-weight:500}
.step-text{top:646px;width:128px;font-size:6px;line-height:1.9;color:var(--muted)}

/* better way */
.grey-band{left:0;top:725px;width:632px;height:278px;background:var(--grey)}
.shadow-frame{background:var(--pink)}
.photo{background:linear-gradient(135deg,#8b6b4e,#c79a80 45%,#d8b79c 70%,#6c4e3b)}
.label{font-size:7px;color:var(--pink-label);font-weight:500}
.h2{font-family:"Nunito",sans-serif;font-weight:600;font-size:13.5px;line-height:1.55}
.feat{left:352px;display:flex;align-items:center;gap:12px;font-size:8px;color:var(--muted)}
.feat-icon{position:relative;width:22px;height:20px}
.feat-icon::before{content:"";position:absolute;left:0;bottom:0;width:11px;height:11px;border-radius:50%;background:var(--pink)}
.feat-icon svg{position:relative;width:20px;height:20px;margin-left:2px}

/* pink promo */
.promo{left:0;top:1003px;width:632px;height:155px;background:var(--pink)}
.promo-title{top:1029px}
.promo-rule{left:268px;top:1058px;width:96px;height:2px;background:var(--ink)}
.promo-text{left:0;width:632px;top:1078px;text-align:center;font-size:6.5px}
.promo-btn{left:271px;top:1104px;background:var(--ink);color:var(--white)}

/* how it works */
.how-list{left:76px;top:1273px;width:200px;list-style:none;font-size:5.8px;color:var(--muted)}
.how-list li{position:relative;padding-left:14px;margin-bottom:8px;line-height:1.8}
.how-list li::before{content:"♥";position:absolute;left:0;top:0;font-size:7px;color:var(--pink-line)}
.how-list li.sub{padding-left:24px}
.how-list li.sub::before{content:"";left:10px;top:3px;width:5px;height:5px;border-radius:50%;border:1px solid var(--pink-line)}
.photo-warm{background:linear-gradient(135deg,#e6b36c,#c85a3c 45%,#a42230 65%,#3c4b5a)}

/* faq */
.faq-band{left:0;top:1448px;width:632px;height:300px;background:var(--grey)}
.pill{width:229px;height:25px;background:var(--white);border-radius:13px;box-shadow:0 1px 3px rgba(0,0,0,.12);display:flex;align-items:center;justify-content:space-between;padding:0 8px 0 12px;font-size:7px;white-space:nowrap}
.pill svg{width:11px;height:11px;flex:none}
.faq-answer{left:338px;top:1568px;width:217px;font-size:6.1px;line-height:1.85;color:var(--muted);text-align:justify}

/* contact */
.contact{left:0;top:1748px;width:632px;height:332px;background:var(--night)}
.contact-title{top:1772px;color:var(--white)}
.contact-rule{left:280px;top:1796px;width:72px;height:2px;background:var(--pink)}
.field{width:184px;height:24px;border-bottom:1px solid var(--line-dark);font-size:6.5px;padding:8px 0 0 12px;color:var(--light)}
.submit{left:275px;top:1950px;background:var(--pink);color:var(--ink);font-size:6.5px;padding:6px 14px}
.info{top:1994px;display:flex;gap:8px;align-items:flex-start;color:var(--white)}
.info i{width:22px;height:22px;border-radius:50%;background:var(--pink);display:flex;align-items:center;justify-content:center;flex:none}
.info i svg{width:11px;height:11px}
.info b{display:block;font-family:"Nunito",sans-serif;font-weight:600;font-size:9.5px;color:var(--white)}
.info span{display:block;font-size:6px;margin-top:4px;color:var(--light)}
.copyright{left:0;width:632px;top:2060px;text-align:center;font-size:6.3px;color:var(--light)}
</style>
</head>
<body>

<!-- concept A -->
<div class="page page--a">
  <div class="abs topline"></div>
  <div class="abs brand"><span class="brand-dot"></span>Larkspin Date</div>
  <div class="abs contact-item" style="left:224px"><svg viewBox="0 0 20 20"><rect x="2" y="5" width="16" height="11" rx="1" fill="none" stroke="#1a1a1a" stroke-width="1.6"/><path d="M2 6l8 6 8-6" fill="none" stroke="#1a1a1a" stroke-width="1.6"/></svg><div><small>Email Address:</small><b>welcome@larkspindate.com</b></div></div>
  <div class="abs contact-item" style="left:380px"><svg viewBox="0 0 20 20"><path d="M4 3l3 0 2 4-2 2c1 2 3 4 5 5l2-2 4 2 0 3c-7 1-15-7-14-14z" fill="#1a1a1a"/></svg><div><small>Call Us:</small><b>(555) 310-4472</b></div></div>
  <div class="abs socials"><span></span><span></span><span></span></div>
  <div class="abs nav"><a style="left:48px">Home</a><a style="left:137px">Event Locations</a><a style="left:259px">How it Works</a><a style="left:372px">FAQ</a></div>

  <div class="abs hero-photo" role="img" aria-label="Photo of a smiling couple outdoors"></div>
  <div class="abs hero-title">STOP SWIPING, START DATING!</div>
  <div class="abs hero-sub">Our events are speed-dating made fresh, modern, and highly enjoyable.</div>
  <div class="abs btn hero-btn">Click To Join <svg viewBox="0 0 10 10"><circle cx="5" cy="5" r="5" fill="#1a1a1a"/><path d="M4 3l2 2-2 2" stroke="#fff" fill="none"/></svg></div>

  <div class="abs card" style="left:76px"><svg viewBox="0 0 26 26"><circle cx="13" cy="14" r="10" fill="none" stroke="#1a1a1a" stroke-width="1.6"/><path d="M13 8v6l4 2" stroke="#1a1a1a" stroke-width="1.6" fill="none"/></svg>7 ROUNDS</div>
  <div class="abs card card--active" style="left:240px"><svg viewBox="0 0 26 26"><circle cx="13" cy="10" r="7" fill="none" stroke="#1a1a1a" stroke-width="1.6"/><path d="M9 16l-2 8 6-3 6 3-2-8" fill="none" stroke="#1a1a1a" stroke-width="1.6"/></svg>7 DATES</div>
  <div class="abs card" style="left:404px"><svg viewBox="0 0 26 26"><rect x="6" y="3" width="14" height="20" rx="1" fill="none" stroke="#1a1a1a" stroke-width="1.6"/><path d="M9 10h8M9 14h8M9 18h5" stroke="#1a1a1a" stroke-width="1.4"/></svg>7 OPPORTUNITIES<br>FOR SOMETHING NEW</div>
  <div class="abs intro">Each event consists of 7 rounds, at 10 minutes each. This gives each date enough time to build an organic rapport, and really get a sense of each other's vibe. Rather than just going through the motions, you'll be able to have an honest and interesting conversation.</div>

  <div class="abs section-title" style="top:496px">CASUAL IS OUR CODE</div>
  <div class="abs rule" style="top:521px"></div>
  <svg class="abs code-icon" style="left:77px;width:62px" viewBox="0 0 62 52" aria-label="Clothes rack icon"><path d="M4 6h54M8 6v44M54 6v44M4 50h8M50 50h8" stroke="#1a1a1a" stroke-width="3" fill="none"/><path d="M14 12l6-4 6 4 2 30h-16z" fill="#1a1a1a"/><path d="M30 12l6-4 6 4 2 30h-16z" fill="#1a1a1a" stroke="#fff" stroke-width="1.5"/><path d="M20 8v-3M36 8v-3" stroke="#1a1a1a" stroke-width="2"/></svg>
  <div class="abs dash" style="left:162px"></div>
  <svg class="abs code-icon" style="left:272px;width:82px" viewBox="0 0 82 52" aria-label="Two chairs icon"><path d="M4 20h6v18h20v12h-4v-8H10v8H4z" fill="#1a1a1a"/><rect x="14" y="24" width="10" height="12" rx="2" fill="#1a1a1a"/><circle cx="19" cy="16" r="4" fill="#1a1a1a"/><path d="M78 20h-6v18H52v12h4v-8h16v8h6z" fill="#1a1a1a"/><rect x="58" y="24" width="10" height="12" rx="2" fill="#1a1a1a"/><circle cx="63" cy="16" r="4" fill="#1a1a1a"/></svg>
  <div class="abs dash" style="left:372px"></div>
  <svg class="abs" style="left:474px;top:554px;width:68px;height:52px" viewBox="0 0 68 52"><path d="M40 6c5-7 18-4 16 7-2 8-12 14-12 14S30 20 30 12c0-7 6-9 10-6z" fill="#1a1a1a"/><path d="M20 12c6-8 22-4 20 9-2 11-18 25-18 25S2 32 2 20c0-10 11-14 18-8z" fill="#1a1a1a" stroke="#fff" stroke-width="2"/></svg>
  <div class="abs step-num" style="left:37px">01</div>
  <div class="abs step-title" style="left:81px">Casual Dress</div>
  <div class="abs step-text" style="left:81px">Show up to your dates in whatever you feel most comfortable in, be it business casual or your favorite sweater.</div>
  <div class="abs step-num" style="left:221px">02</div>
  <div class="abs step-title" style="left:265px">Casual Conversation</div>
  <div class="abs step-text" style="left:265px">You'll be on multiple, short(ish) dates – don't waste that precious time on formalities! You can catch-up on details later if you both.</div>
  <div class="abs step-num" style="left:418px">03</div>
  <div class="abs step-title" style="left:463px">Casual Dates</div>
  <div class="abs step-text" style="left:463px">Our events are meant to be as simple as a casual conversation. Instead of the formalities and heaviness.</div>

  <div class="abs grey-band"></div>
  <div class="abs shadow-frame" style="left:66px;top:770px;width:224px;height:196px"></div>
  <div class="abs photo" role="img" aria-label="Photo of a man and woman chatting at a café table" style="left:76px;top:761px;width:224px;height:196px"></div>
  <div class="abs label" style="left:347px;top:773px">ARE YOU SINGLE?</div>
  <div class="abs h2" style="left:347px;top:788px">THERE'S A BETTER WAY TO<br>ACTUALLY MEET PEOPLE:</div>
  <div class="abs feat" style="top:843px"><span class="feat-icon"><svg viewBox="0 0 20 20"><path d="M3 9h14M6 9v9M14 9v9M2 5v13M18 5v13M2 12h3M15 12h3" stroke="#1a1a1a" stroke-width="1.2" fill="none"/></svg></span>Larkspin Dating</div>
  <div class="abs feat" style="top:879px"><span class="feat-icon"><svg viewBox="0 0 20 20"><path d="M4 8h10v5a4 4 0 0 1-4 4H8a4 4 0 0 1-4-4z" fill="none" stroke="#1a1a1a" stroke-width="1.2"/><path d="M14 9h2a2 2 0 0 1 0 4h-2M2 18h14" stroke="#1a1a1a" stroke-width="1.2" fill="none"/></svg></span>Speed dating as casual as a coffee meet</div>
  <div class="abs feat" style="top:914px"><span class="feat-icon"><svg viewBox="0 0 20 20"><rect x="3" y="4" width="14" height="13" rx="1" fill="none" stroke="#1a1a1a" stroke-width="1.2"/><path d="M3 8h14M7 2v4M13 2v4M6 11h2M9 11h2M12 11h2M6 14h2M9 14h2" stroke="#1a1a1a" stroke-width="1.2"/></svg></span>Find an event near you and start dating.</div>

  <div class="abs promo"></div>
  <div class="abs section-title promo-title">OUR EVENTS FILL UP FAST. DON'T MISS OUT.</div>
  <div class="abs promo-rule"></div>
  <div class="abs promo-text">Join our monthly newsletter to see all events for that month.</div>
  <div class="abs btn promo-btn">Click To Join <svg viewBox="0 0 10 10"><circle cx="5" cy="5" r="5" fill="#fff"/><path d="M4 3l2 2-2 2" stroke="#1a1a1a" fill="none"/></svg></div>

  <div class="abs label" style="left:76px;top:1207px">HOW IT WORKS</div>
  <div class="abs" style="left:76px;top:1226px;font-size:8px;color:var(--muted)">No hosts, no name tags - we like to keep things natural</div>
  <div class="abs h2" style="left:76px;top:1245px">EACH EVENT IS AS SIMPLE AS:</div>
  <ul class="abs how-list" style="width:240px">
    <li>Arrive at your designated time and venue</li>
    <li>Follow our personalized instructions texted to your phone telling you:</li>
    <li class="sub">What time each round starts and ends.</li>
    <li class="sub">A description of who you'll be dating.</li>
    <li>Find your date, find a seat, and start chatting!</li>
    <li>Once your round is over, simply text back whether you found a Match! (M) or a Pass (P)</li>
    <li>Repeat and have fun!</li>
  </ul>
  <div class="abs shadow-frame" style="left:341px;top:1240px;width:224px;height:166px"></div>
  <div class="abs photo-warm" role="img" aria-label="Photo of a couple at sunset holding a heart balloon" style="left:331px;top:1200px;width:224px;height:196px"></div>

  <div class="abs faq-band"></div>
  <div class="abs section-title" style="top:1483px">FREQUENTLY ASKED QUESTIONS</div>
  <div class="abs rule" style="top:1512px;left:242px;width:148px"></div>
  <div class="abs pill" style="left:76px;top:1534px">What are the rules? <svg viewBox="0 0 12 12"><circle cx="6" cy="6" r="6"/><path d="M5 3.5l2.5 2.5L5 8.5" stroke="#fff" fill="none"/></svg></div>
  <div class="abs pill" style="left:76px;top:1571px">How many dates will I go on? <svg viewBox="0 0 12 12"><circle cx="6" cy="6" r="6"/><path d="M5 3.5l2.5 2.5L5 8.5" stroke="#fff" fill="none"/></svg></div>
  <div class="abs pill" style="left:76px;top:1608px">How long do I have on each date? <svg viewBox="0 0 12 12"><circle cx="6" cy="6" r="6"/><path d="M5 3.5l2.5 2.5L5 8.5" stroke="#fff" fill="none"/></svg></div>
  <div class="abs pill" style="left:76px;top:1645px">What happens at the end of each date? <svg viewBox="0 0 12 12"><circle cx="6" cy="6" r="6"/><path d="M5 3.5l2.5 2.5L5 8.5" stroke="#fff" fill="none"/></svg></div>
  <div class="abs pill" style="left:76px;top:1682px">I met someone I wanted to Match with, now what? <svg viewBox="0 0 12 12"><circle cx="6" cy="6" r="6"/><path d="M5 3.5l2.5 2.5L5 8.5" stroke="#fff" fill="none"/></svg></div>
  <div class="abs pill" style="left:326px;top:1534px">What is your cancellation / no-show policy? <svg viewBox="0 0 12 12"><circle cx="6" cy="6" r="6" fill="#fbc9dd"/><path d="M3.5 5l2.5 2.5L8.5 5" stroke="#fff" fill="none"/></svg></div>
  <div class="abs faq-answer">Because crafting an exceptional experience for all participants is paramount, our cancellation policy reflects the dedication to maintaining the quality of our events.</div>
  <div class="abs pill" style="left:326px;top:1608px">Are there breaks in-between each date? <svg viewBox="0 0 12 12"><circle cx="6" cy="6" r="6"/><path d="M5 3.5l2.5 2.5L5 8.5" stroke="#fff" fill="none"/></svg></div>
  <div class="abs pill" style="left:326px;top:1645px">I can't seem to find my date. What should I do? <svg viewBox="0 0 12 12"><circle cx="6" cy="6" r="6"/><path d="M5 3.5l2.5 2.5L5 8.5" stroke="#fff" fill="none"/></svg></div>
  <div class="abs pill" style="left:326px;top:1682px">Is Larkspin partnered with their venues? <svg viewBox="0 0 12 12"><circle cx="6" cy="6" r="6"/><path d="M5 3.5l2.5 2.5L5 8.5" stroke="#fff" fill="none"/></svg></div>

  <div class="abs contact"></div>
  <div class="abs section-title contact-title">CONTACT US</div>
  <div class="abs contact-rule"></div>
  <div class="abs field" style="left:126px;top:1816px">First name</div>
  <div class="abs field" style="left:320px;top:1816px">Last name</div>
  <div class="abs field" style="left:126px;top:1854px">Email</div>
  <div class="abs field" style="left:320px;top:1854px">Phone</div>
  <div class="abs field" style="left:126px;top:1908px;width:378px">Message</div>
  <div class="abs btn submit">SUBMIT NOW <svg viewBox="0 0 10 10"><circle cx="5" cy="5" r="5" fill="#1a1a1a"/><path d="M4 3l2 2-2 2" stroke="#fff" fill="none"/></svg></div>
  <div class="abs info" style="left:103px"><i><svg viewBox="0 0 12 12"><path d="M6 1a3.5 3.5 0 0 1 3.5 3.5C9.5 7 6 11 6 11S2.5 7 2.5 4.5A3.5 3.5 0 0 1 6 1z" fill="#1a1a1a"/><circle cx="6" cy="4.5" r="1.2" fill="#fbc9dd"/></svg></i><div><b>EVENT LOCATIONS :</b><span>Riverton City, RC ▾</span></div></div>
  <div class="abs info" style="left:267px"><i><svg viewBox="0 0 12 12"><path d="M2.5 1.5h2l1 2.5-1.2 1.2c.7 1.3 1.7 2.3 3 3L8.5 7l2.5 1v2C6 10.5 1.5 6 2.5 1.5z" fill="#1a1a1a"/></svg></i><div><b>PHONE :</b><span>(555) 310-4472</span></div></div>
  <div class="abs info" style="left:403px"><i><svg viewBox="0 0 12 12"><rect x="1.5" y="3" width="9" height="6.5" rx=".6" fill="#1a1a1a"/><path d="M1.5 3.5L6 7l4.5-3.5" stroke="#fbc9dd" fill="none"/></svg></i><div><b>EMAIL :</b><span>welcome@larkspindate.com</span></div></div>
  <div class="abs copyright">Copyright © 2024 Larkspin Date. All Rights Reserved.</div>
</div>

<!-- concept B -->
<div class="page page--b">
  <div class="abs topline"></div>
  <div class="abs brand"><span class="brand-dot"></span>Larkspin Date</div>
  <div class="abs contact-item" style="left:224px"><svg viewBox="0 0 20 20"><rect x="2" y="5" width="16" height="11" rx="1" fill="none" stroke="#1a1a1a" stroke-width="1.6"/><path d="M2 6l8 6 8-6" fill="none" stroke="#1a1a1a" stroke-width="1.6"/></svg><div><small>Email Address:</small><b>welcome@larkspindate.com</b></div></div>
  <div class="abs contact-item" style="left:380px"><svg viewBox="0 0 20 20"><path d="M4 3l3 0 2 4-2 2c1 2 3 4 5 5l2-2 4 2 0 3c-7 1-15-7-14-14z" fill="#1a1a1a"/></svg><div><small>Call Us:</small><b>(555) 310-4472</b></div></div>
  <div class="abs socials"><span></span><span></span><span></span></div>
  <div class="abs nav"><a style="left:48px">Home</a><a style="left:137px">Event Locations</a><a style="left:259px">How it Works</a><a style="left:372px">FAQ</a></div>

  <div class="abs hero-photo" role="img" aria-label="Photo of a couple embracing with red heart balloons on a bridge"></div>
  <div class="abs hero-title">STOP SWIPING, START DATING!</div>
  <div class="abs hero-sub">Our events are speed-dating made fresh, modern, and highly enjoyable.</div>
  <div class="abs btn hero-btn">Click To Join <svg viewBox="0 0 10 10"><circle cx="5" cy="5" r="5" fill="#1a1a1a"/><path d="M4 3l2 2-2 2" stroke="#fff" fill="none"/></svg></div>

  <div class="abs card" style="left:76px"><svg viewBox="0 0 26 26"><circle cx="13" cy="14" r="10" fill="none" stroke="#1a1a1a" stroke-width="1.6"/><path d="M13 8v6l4 2" stroke="#1a1a1a" stroke-width="1.6" fill="none"/></svg>7 ROUNDS</div>
  <div class="abs card card--active" style="left:240px"><svg viewBox="0 0 26 26"><circle cx="13" cy="10" r="7" fill="none" stroke="#1a1a1a" stroke-width="1.6"/><path d="M9 16l-2 8 6-3 6 3-2-8" fill="none" stroke="#1a1a1a" stroke-width="1.6"/></svg>7 DATES</div>
  <div class="abs card" style="left:404px"><svg viewBox="0 0 26 26"><rect x="6" y="3" width="14" height="20" rx="1" fill="none" stroke="#1a1a1a" stroke-width="1.6"/><path d="M9 10h8M9 14h8M9 18h5" stroke="#1a1a1a" stroke-width="1.4"/></svg>7 OPPORTUNITIES<br>FOR SOMETHING NEW</div>
  <div class="abs intro">Each event consists of 7 rounds, at 10 minutes each. This gives each date enough time to build an organic rapport, and really get a sense of each other's vibe. Rather than just going through the motions, you'll be able to have an honest and interesting conversation.</div>

  <div class="abs section-title" style="top:496px">CASUAL IS OUR CODE</div>
  <div class="abs rule" style="top:521px"></div>
  <svg class="abs code-icon" style="left:77px;width:62px" viewBox="0 0 62 52" aria-label="Clothes rack icon"><path d="M4 6h54M8 6v44M54 6v44M4 50h8M50 50h8" stroke="#1a1a1a" stroke-width="3" fill="none"/><path d="M14 12l6-4 6 4 2 30h-16z" fill="#1a1a1a"/><path d="M30 12l6-4 6 4 2 30h-16z" fill="#1a1a1a" stroke="#fff" stroke-width="1.5"/><path d="M20 8v-3M36 8v-3" stroke="#1a1a1a" stroke-width="2"/></svg>
  <div class="abs dash" style="left:162px"></div>
  <svg class="abs code-icon" style="left:272px;width:82px" viewBox="0 0 82 52" aria-label="Two chairs icon"><path d="M4 20h6v18h20v12h-4v-8H10v8H4z" fill="#1a1a1a"/><rect x="14" y="24" width="10" height="12" rx="2" fill="#1a1a1a"/><circle cx="19" cy="16" r="4" fill="#1a1a1a"/><path d="M78 20h-6v18H52v12h4v-8h16v8h6z" fill="#1a1a1a"/><rect x="58" y="24" width="10" height="12" rx="2" fill="#1a1a1a"/><circle cx="63" cy="16" r="4" fill="#1a1a1a"/></svg>
  <div class="abs dash" style="left:372px"></div>
  <svg class="abs" style="left:474px;top:554px;width:68px;height:52px" viewBox="0 0 68 52"><path d="M40 6c5-7 18-4 16 7-2 8-12 14-12 14S30 20 30 12c0-7 6-9 10-6z" fill="#1a1a1a"/><path d="M20 12c6-8 22-4 20 9-2 11-18 25-18 25S2 32 2 20c0-10 11-14 18-8z" fill="#1a1a1a" stroke="#fff" stroke-width="2"/></svg>
  <div class="abs step-num" style="left:37px">01</div>
  <div class="abs step-title" style="left:81px">Casual Dress</div>
  <div class="abs step-text" style="left:81px">Show up to your dates in whatever you feel most comfortable in, be it business casual or your favorite sweater.</div>
  <div class="abs step-num" style="left:221px">02</div>
  <div class="abs step-title" style="left:265px">Casual Conversation</div>
  <div class="abs step-text" style="left:265px">You'll be on multiple, short(ish) dates – don't waste that precious time on formalities! You can catch-up on details later if you both.</div>
  <div class="abs step-num" style="left:418px">03</div>
  <div class="abs step-title" style="left:463px">Casual Dates</div>
  <div class="abs step-text" style="left:463px">Our events are meant to be as simple as a casual conversation. Instead of the formalities and heaviness.</div>

  <div class="abs grey-band"></div>
  <div class="abs shadow-frame" style="left:66px;top:770px;width:224px;height:196px"></div>
  <div class="abs photo" role="img" aria-label="Photo of a man and woman chatting at a café table" style="left:76px;top:761px;width:224px;height:196px"></div>
  <div class="abs label" style="left:347px;top:773px">ARE YOU SINGLE?</div>
  <div class="abs h2" style="left:347px;top:788px">THERE'S A BETTER WAY TO<br>ACTUALLY MEET PEOPLE:</div>
  <div class="abs feat" style="top:843px"><span class="feat-icon"><svg viewBox="0 0 20 20"><path d="M3 9h14M6 9v9M14 9v9M2 5v13M18 5v13M2 12h3M15 12h3" stroke="#1a1a1a" stroke-width="1.2" fill="none"/></svg></span>Larkspin Dating</div>
  <div class="abs feat" style="top:879px"><span class="feat-icon"><svg viewBox="0 0 20 20"><path d="M4 8h10v5a4 4 0 0 1-4 4H8a4 4 0 0 1-4-4z" fill="none" stroke="#1a1a1a" stroke-width="1.2"/><path d="M14 9h2a2 2 0 0 1 0 4h-2M2 18h14" stroke="#1a1a1a" stroke-width="1.2" fill="none"/></svg></span>Speed dating as casual as a coffee meet</div>
  <div class="abs feat" style="top:914px"><span class="feat-icon"><svg viewBox="0 0 20 20"><rect x="3" y="4" width="14" height="13" rx="1" fill="none" stroke="#1a1a1a" stroke-width="1.2"/><path d="M3 8h14M7 2v4M13 2v4M6 11h2M9 11h2M12 11h2M6 14h2M9 14h2" stroke="#1a1a1a" stroke-width="1.2"/></svg></span>Find an event near you and start dating.</div>

  <div class="abs promo"></div>
  <div class="abs section-title promo-title">OUR EVENTS FILL UP FAST. DON'T MISS OUT.</div>
  <div class="abs promo-rule"></div>
  <div class="abs promo-text">Join our monthly newsletter to see all events for that month.</div>
  <div class="abs btn promo-btn">Click To Join <svg viewBox="0 0 10 10"><circle cx="5" cy="5" r="5" fill="#fff"/><path d="M4 3l2 2-2 2" stroke="#1a1a1a" fill="none"/></svg></div>

  <div class="abs label" style="left:76px;top:1207px">HOW IT WORKS</div>
  <div class="abs" style="left:76px;top:1226px;font-size:8px;color:var(--muted)">No hosts, no name tags - we like to keep things natural</div>
  <div class="abs h2" style="left:76px;top:1245px">EACH EVENT IS AS SIMPLE AS:</div>
  <ul class="abs how-list" style="width:240px">
    <li>Arrive at your designated time and venue</li>
    <li>Follow our personalized instructions texted to your phone telling you:</li>
    <li class="sub">What time each round starts and ends.</li>
    <li class="sub">A description of who you'll be dating.</li>
    <li>Find your date, find a seat, and start chatting!</li>
    <li>Once your round is over, simply text back whether you found a Match! (M) or a Pass (P)</li>
    <li>Repeat and have fun!</li>
  </ul>
  <div class="abs shadow-frame" style="left:341px;top:1240px;width:224px;height:166px"></div>
  <div class="abs photo-warm" role="img" aria-label="Photo of a couple at sunset holding a heart balloon" style="left:331px;top:1200px;width:224px;height:196px"></div>

  <div class="abs faq-band"></div>
  <div class="abs section-title" style="top:1483px">FREQUENTLY ASKED QUESTIONS</div>
  <div class="abs rule" style="top:1512px;left:242px;width:148px"></div>
  <div class="abs pill" style="left:76px;top:1534px">What are the rules? <svg viewBox="0 0 12 12"><circle cx="6" cy="6" r="6"/><path d="M5 3.5l2.5 2.5L5 8.5" stroke="#fff" fill="none"/></svg></div>
  <div class="abs pill" style="left:76px;top:1571px">How many dates will I go on? <svg viewBox="0 0 12 12"><circle cx="6" cy="6" r="6"/><path d="M5 3.5l2.5 2.5L5 8.5" stroke="#fff" fill="none"/></svg></div>
  <div class="abs pill" style="left:76px;top:1608px">How long do I have on each date? <svg viewBox="0 0 12 12"><circle cx="6" cy="6" r="6"/><path d="M5 3.5l2.5 2.5L5 8.5" stroke="#fff" fill="none"/></svg></div>
  <div class="abs pill" style="left:76px;top:1645px">What happens at the end of each date? <svg viewBox="0 0 12 12"><circle cx="6" cy="6" r="6"/><path d="M5 3.5l2.5 2.5L5 8.5" stroke="#fff" fill="none"/></svg></div>
  <div class="abs pill" style="left:76px;top:1682px">I met someone I wanted to Match with, now what? <svg viewBox="0 0 12 12"><circle cx="6" cy="6" r="6"/><path d="M5 3.5l2.5 2.5L5 8.5" stroke="#fff" fill="none"/></svg></div>
  <div class="abs pill" style="left:326px;top:1534px">What is your cancellation / no-show policy? <svg viewBox="0 0 12 12"><circle cx="6" cy="6" r="6" fill="#fbc9dd"/><path d="M3.5 5l2.5 2.5L8.5 5" stroke="#fff" fill="none"/></svg></div>
  <div class="abs faq-answer">Because crafting an exceptional experience for all participants is paramount, our cancellation policy reflects the dedication to maintaining the quality of our events.</div>
  <div class="abs pill" style="left:326px;top:1608px">Are there breaks in-between each date? <svg viewBox="0 0 12 12"><circle cx="6" cy="6" r="6"/><path d="M5 3.5l2.5 2.5L5 8.5" stroke="#fff" fill="none"/></svg></div>
  <div class="abs pill" style="left:326px;top:1645px">I can't seem to find my date. What should I do? <svg viewBox="0 0 12 12"><circle cx="6" cy="6" r="6"/><path d="M5 3.5l2.5 2.5L5 8.5" stroke="#fff" fill="none"/></svg></div>
  <div class="abs pill" style="left:326px;top:1682px">Is Larkspin partnered with their venues? <svg viewBox="0 0 12 12"><circle cx="6" cy="6" r="6"/><path d="M5 3.5l2.5 2.5L5 8.5" stroke="#fff" fill="none"/></svg></div>

  <div class="abs contact"></div>
  <div class="abs section-title contact-title">CONTACT US</div>
  <div class="abs contact-rule"></div>
  <div class="abs field" style="left:126px;top:1816px">First name</div>
  <div class="abs field" style="left:320px;top:1816px">Last name</div>
  <div class="abs field" style="left:126px;top:1854px">Email</div>
  <div class="abs field" style="left:320px;top:1854px">Phone</div>
  <div class="abs field" style="left:126px;top:1908px;width:378px">Message</div>
  <div class="abs btn submit">SUBMIT NOW <svg viewBox="0 0 10 10"><circle cx="5" cy="5" r="5" fill="#1a1a1a"/><path d="M4 3l2 2-2 2" stroke="#fff" fill="none"/></svg></div>
  <div class="abs info" style="left:103px"><i><svg viewBox="0 0 12 12"><path d="M6 1a3.5 3.5 0 0 1 3.5 3.5C9.5 7 6 11 6 11S2.5 7 2.5 4.5A3.5 3.5 0 0 1 6 1z" fill="#1a1a1a"/><circle cx="6" cy="4.5" r="1.2" fill="#fbc9dd"/></svg></i><div><b>EVENT LOCATIONS :</b><span>Riverton City, RC ▾</span></div></div>
  <div class="abs info" style="left:267px"><i><svg viewBox="0 0 12 12"><path d="M2.5 1.5h2l1 2.5-1.2 1.2c.7 1.3 1.7 2.3 3 3L8.5 7l2.5 1v2C6 10.5 1.5 6 2.5 1.5z" fill="#1a1a1a"/></svg></i><div><b>PHONE :</b><span>(555) 310-4472</span></div></div>
  <div class="abs info" style="left:403px"><i><svg viewBox="0 0 12 12"><rect x="1.5" y="3" width="9" height="6.5" rx=".6" fill="#1a1a1a"/><path d="M1.5 3.5L6 7l4.5-3.5" stroke="#fbc9dd" fill="none"/></svg></i><div><b>EMAIL :</b><span>welcome@larkspindate.com</span></div></div>
  <div class="abs copyright">Copyright © 2024 Larkspin Date. All Rights Reserved.</div>
</div>

</body>
</html>
```